Corwick Habitat Web

We just need an update/re-design of our existing web site that would include our new company logo and some new photo's. Our current web site can be viewed at www.corwickhabitat.com.au. We would require something very similar to what we have at the moment in terms of content it should all be the same.
The web site would basically act more as a portfolio than one that would generate more business.
We are after a very modern and simple design and maybe something where we can upload our own project photo's and project descriptions as we complete them.

Industry/Entity Type

It Company

```html
<!DOCTYPE html>
<html lang="en">
<head>
<meta charset="utf-8">
<title>Corwick Habitat</title>
<link rel="stylesheet" href="https://fonts.googleapis.com/css2?family=Raleway:wght@300;400&display=swap">
<style>
  :root {
    --ink: #3a3a3c;
    --muted: #8e8e90;
    --rule: #e8e8e8;
    --accent: #2b2b2d;
    --footer: #333438;
    --footer-text: #ffffff;
    --footer-muted: #9a9a9e;
    --sky: #c9cbcf;
    --steel: #6d7075;
    --navy: #26293a;
  }
  * { box-sizing: border-box; margin: 0; padding: 0; }
  html, body { width: 1077px; height: 1200px; overflow: hidden; background: #fff; }
  body { position: relative; font-family: 'Raleway', sans-serif; font-weight: 300; color: var(--ink); }
  .abs { position: absolute; }

  .brand { font-weight: 300; font-size: 29px; letter-spacing: 0.2px; color: var(--ink); white-space: nowrap; }
  .nav { display: flex; gap: 0; font-size: 10px; font-weight: 400; color: var(--muted); white-space: nowrap; }
  .nav a { color: inherit; text-decoration: none; }
  .nav .sep { margin: 0 20px; }

  .photo { display: block; }
  .hero-1 { background: linear-gradient(180deg, #d4d6d9 0%, #b9bcc0 45%, #55585d 70%, #3a3c40 100%); }
  .hero-2 { background: linear-gradient(160deg, #d2d4d7 0%, #a9acb1 40%, #56595e 70%, #2f3135 100%); }
  .hero-3 { background: linear-gradient(180deg, #e9e8e4 0%, #b9a58b 35%, #cfccc5 65%, #8b8470 100%); }
  .thumb-a { background: linear-gradient(180deg, #6f7276 0%, #a0653a 50%, #9a9b9d 100%); }
  .thumb-b { background: linear-gradient(180deg, #5f87c9 0%, #3d4d5e 55%, #6b3f2c 100%); }
  .thumb-c { background: linear-gradient(160deg, #dfe2e6 0%, #2c3040 40%, #23263a 100%); }

  .heading { font-size: 16.5px; font-weight: 400; color: var(--ink); }
  .bar { width: 40px; height: 2px; background: var(--accent); }
  .copy { font-size: 10.6px; line-height: 16.1px; color: var(--muted); }
  .divider { height: 1px; background: var(--rule); }

  .overlay-icon { width: 28px; height: 28px; border: 1px solid #fff; display: flex; align-items: center; justify-content: center; }

  .site-footer { left: 0; top: 1065px; width: 1077px; height: 135px; background: var(--footer); }
  .site-footer .brand { color: var(--footer-text); }
  .site-footer .nav { color: var(--footer-text); }
  .copyright { font-size: 8.4px; color: var(--footer-muted); }
</style>
</head>
<body>

<header>
  <div class="abs brand" style="left:144px; top:34px;">Corwick Habitat</div>
  <nav class="abs nav" style="left:599px; top:43px;">
    <a href="#">Home</a><span class="sep">/</span>
    <a href="#">Recent Projects</a><span class="sep">/</span>
    <a href="#">Our Services</a><span class="sep">/</span>
    <a href="#">Contact Us</a>
  </nav>
</header>

<section class="hero">
  <div class="abs photo hero-1" role="img" aria-label="Modern office building facade with louvres under a cloudy sky" style="left:144px; top:100px; width:256px; height:303px;"></div>
  <div class="abs photo hero-2" role="img" aria-label="Cantilevered grey cladding over a glazed entry" style="left:410px; top:100px; width:256px; height:303px;"></div>
  <div class="abs photo hero-3" role="img" aria-label="Interior corridor with timber ceiling battens and patterned carpet" style="left:676px; top:100px; width:256px; height:303px;"></div>
</section>

<section class="about">
  <h2 class="abs heading" style="left:144px; top:466px;">Corwick Habitat Pty Ltd</h2>
  <div class="abs bar" style="left:144px; top:502px;"></div>
  <p class="abs copy" style="left:144px; top:521px; width:384px;">Corwick Habitat Pty Ltd was established in 2005 and has been operating in the Sydney area, but has completed numerous projects<br>outside of Sydney.</p>
  <div class="abs divider" style="left:144px; top:596px; width:384px;"></div>
  <div class="abs photo thumb-a" role="img" aria-label="Building with timber and grey cladding" style="left:144px; top:628px; width:115px; height:114px;"></div>
  <div class="abs photo thumb-b" role="img" aria-label="Glazed curtain wall reflecting blue sky" style="left:279px; top:628px; width:115px; height:114px;"></div>
  <div class="abs photo thumb-c" role="img" aria-label="Dark navy panel facade" style="left:414px; top:628px; width:114px; height:114px;"></div>
</section>

<section class="services">
  <h2 class="abs heading" style="left:548px; top:466px;">We specialise in the internal fit outs to</h2>
  <div class="abs bar" style="left:548px; top:502px;"></div>
  <p class="abs copy" style="left:548px; top:521px; width:384px;">
    - Industrial Offices<br>- Multi Storey Offices<br>- Commercial Projects<br>- Residential Houses<br>- External Facades
  </p>
  <p class="abs copy" style="left:548px; top:618px; width:384px;">The key group of our operating staff have all been involved in the construction industry for well over 20 years.</p>
  <p class="abs copy" style="left:548px; top:666px; width:384px;">Our employees are skilled and trained and have the experience to deliver the best possible product, safely and on time.</p>
  <p class="abs copy" style="left:548px; top:714px; width:384px;">At Corwick Habitat we pride ourselves on working together with our clients in providing the best possible service on schedule and within budget.</p>
</section>

<section class="projects">
  <h2 class="abs heading" style="left:143px; top:805px;">Recent Projects</h2>
  <div class="abs bar" style="left:144px; top:842px;"></div>
  <div class="abs photo hero-1" role="img" aria-label="Office building with louvred facade" style="left:144px; top:863px; width:182px; height:135px;"></div>
  <div class="abs photo thumb-a" role="img" aria-label="Building with timber and grey cladding" style="left:346px; top:863px; width:182px; height:135px;"></div>
  <div class="abs photo" role="img" aria-label="Glazed building facade, darkened on hover" style="left:548px; top:863px; width:182px; height:135px; background:linear-gradient(180deg,#2a2c34 0%,#22242b 100%);">
    <div class="abs overlay-icon" style="left:77px; top:53px;">
      <svg width="12" height="12" viewBox="0 0 12 12"><circle cx="5" cy="5" r="3.4" fill="none" stroke="#fff" stroke-width="1.6"/><line x1="7.5" y1="7.5" x2="10.5" y2="10.5" stroke="#fff" stroke-width="1.8" stroke-linecap="round"/></svg>
    </div>
  </div>
  <div class="abs photo thumb-c" role="img" aria-label="Dark navy panel facade" style="left:750px; top:863px; width:182px; height:135px;"></div>
</section>

<footer class="abs site-footer">
  <div class="abs brand" style="left:144px; top:41px;">Corwick Habitat</div>
  <nav class="abs nav" style="left:599px; top:50px;">
    <a href="#">Home</a><span class="sep">/</span>
    <a href="#">Recent Projects</a><span class="sep">/</span>
    <a href="#">Our Services</a><span class="sep">/</span>
    <a href="#">Contact Us</a>
  </nav>
  <p class="abs copyright" style="left:144px; top:118px;">© Copyright Corwick Habitat Pty Ltd 2014</p>
</footer>

</body>
</html>
```